Updated Dealer Toolbox- Marketing

We need a post card that is marketing a new online resource that is available on our website. This is a Toolbox, which contains many helpful tools and downloads to our clients. We need this post card to have 4 main bullet points on the front, with the logo of our resource toolbox, and on the back- our contact information and how to register.We work in dealerships across the USA that are part of the Outdoor Power Industry (mowers, farm equipment, etc) We would like this to be a classy but easy to read format, as our clients are busy and need to get the point quickly.

My personal contact information: Marisol@tedharwick.net. 816-392-5180
Updates

i have added additional files, and will be adding the logo today. Sorry for the lack of information. Added Wednesday, May 6, 2015

Industry/Entity Type

Marketing

Font styles to use
Serif

Requirements
Must have
• Toolbox attachment on front, contact info on back
Nice to have
• Colors that will attract the eye in the mail
Should not have
• Additional text or designs. Just what is submitted

```html
<!DOCTYPE html>
<html lang="en">
<head>
<meta charset="utf-8">
<title>What's in the Toolbox? – Postcard</title>
<link href="https://fonts.googleapis.com/css2?family=Roboto+Condensed:wght@400;700;900&display=swap" rel="stylesheet">
<style>
  :root {
    --page-bg: #e9e7e4;
    --teal-light: #c9ecea;
    --teal-mid: #8fd0cc;
    --teal-deep: #5aaaa7;
    --tool-red: #c8232b;
    --ink: #141414;
    --bubble: rgba(255, 255, 255, 0.32);
    --brand-green: #1b6a43;
    --card-white: #ffffff;
    --rule-grey: #c9c9c9;
    --stamp-grey: #e4e4e4;
  }
  * { margin: 0; padding: 0; box-sizing: border-box; }
  html, body { width: 1200px; height: 1000px; overflow: hidden; }
  body {
    position: relative;
    background: var(--page-bg);
    font-family: "Roboto Condensed", "Arial Narrow", sans-serif;
    color: var(--ink);
  }

  /* ---------- Front side ---------- */
  .card-front {
    position: absolute;
    left: 75px; top: 40px;
    width: 578px; height: 443px;
    overflow: hidden;
    background:
      radial-gradient(ellipse 55% 70% at 50% 0%, rgba(255,255,255,0.55), rgba(255,255,255,0) 70%),
      linear-gradient(180deg, var(--teal-light) 0%, var(--teal-mid) 55%, var(--teal-deep) 100%);
  }
  .front-title {
    position: absolute;
    top: 20px; left: 0; width: 100%;
    text-align: center;
    font-weight: 900;
    font-size: 50px;
    letter-spacing: -0.5px;
    color: var(--ink);
  }
  .toolbox-art {
    position: absolute;
    left: 140px; top: 100px;
    width: 300px; height: 200px;
    border-radius: 14px;
    background: linear-gradient(180deg, #b8262c 0%, #c9363b 45%, #e8f5f4 70%, #bfe3e1 100%);
  }
  .connectors {
    position: absolute; left: 0; top: 0;
    width: 578px; height: 443px;
  }
  .feature {
    position: absolute;
    border-radius: 50%;
    background: var(--bubble);
    text-align: center;
  }
  .feature-icon {
    display: block;
    margin: 0 auto;
    width: 36px; height: 36px;
  }
  .feature-label {
    display: block;
    margin-top: 8px;
    font-size: 16px;
    line-height: 21px;
    color: var(--ink);
    text-transform: uppercase;
  }
  .feature--webinars { left: 10px;  top: 225px; width: 130px; height: 130px; padding-top: 30px; }
  .feature--jobs     { left: 152px; top: 292px; width: 136px; height: 136px; padding-top: 22px; }
  .feature--rental   { left: 300px; top: 292px; width: 136px; height: 136px; padding-top: 22px; }
  .feature--audio    { left: 440px; top: 225px; width: 130px; height: 130px; padding-top: 30px; }

  /* ---------- Back side ---------- */
  .card-back {
    position: absolute;
    left: 558px; top: 503px;
    width: 590px; height: 459px;
    background: var(--card-white);
    box-shadow: 0 0 0 1px #dcdcdc;
  }
  .brand {
    position: absolute;
    left: 90px; top: 24px;
    display: flex; align-items: center; gap: 8px;
  }
  .brand-mark {
    width: 34px; height: 34px;
    background: var(--brand-green);
  }
  .brand-name {
    font-size: 19px;
    font-weight: 700;
    color: var(--brand-green);
    line-height: 1;
  }
  .message {
    position: absolute;
    left: 12px; top: 86px;
    width: 284px;
    text-align: center;
  }
  .message-headline {
    font-weight: 700;
    font-size: 18.5px;
    line-height: 22px;
    color: var(--ink);
  }
  .message-body {
    margin-top: 6px;
    font-size: 14px;
    line-height: 18px;
    color: var(--ink);
  }
  .contact {
    margin-top: 24px;
    font-weight: 700;
    font-size: 16px;
    line-height: 19px;
  }
  .contact .accent { color: var(--brand-green); }
  .stamp-box {
    position: absolute;
    left: 460px; top: 22px;
    width: 106px; height: 123px;
    border: 3px solid var(--stamp-grey);
  }
  .address-lines {
    position: absolute;
    left: 310px; top: 211px;
    width: 250px;
    list-style: none;
  }
  .address-lines li {
    height: 36px;
    border-top: 2px solid var(--rule-grey);
  }
</style>
</head>
<body>

<section class="card-front" aria-label="Postcard front">
  <h1 class="front-title">What’s in the Toolbox?</h1>

  <div class="toolbox-art" role="img" aria-label="Illustration of a red toolbox labelled TOOLS with a computer mouse on a white pedestal"></div>

  <svg class="connectors" viewBox="0 0 578 443" aria-hidden="true">
    <g fill="none" stroke="#d8262e" stroke-width="1.2" stroke-dasharray="3 3">
      <polyline points="75,255 75,170 185,170"/>
      <polyline points="385,170 510,170 510,255"/>
      <line x1="220" y1="240" x2="220" y2="314"/>
      <line x1="365" y1="240" x2="365" y2="314"/>
    </g>
  </svg>

  <div class="feature feature--webinars">
    <svg class="feature-icon" viewBox="0 0 36 36" aria-hidden="true">
      <circle cx="18" cy="18" r="16" fill="#fff" stroke="#d8262e" stroke-width="3"/>
      <circle cx="18" cy="16" r="6" fill="none" stroke="#222" stroke-width="2"/>
      <circle cx="18" cy="16" r="2" fill="#222"/>
      <path d="M13 25h10l-2-3h-6z" fill="#222"/>
    </svg>
    <span class="feature-label">Webinars</span>
  </div>

  <div class="feature feature--jobs">
    <svg class="feature-icon" viewBox="0 0 36 36" aria-hidden="true">
      <circle cx="18" cy="18" r="16" fill="#fff" stroke="#d8262e" stroke-width="3"/>
      <path d="M10 13h6l2 2h8v10H10z" fill="#222"/>
    </svg>
    <span class="feature-label">Job<br>Descriptions</span>
  </div>

  <div class="feature feature--rental">
    <svg class="feature-icon" viewBox="0 0 36 36" aria-hidden="true">
      <circle cx="18" cy="18" r="16" fill="#fff" stroke="#d8262e" stroke-width="3"/>
      <rect x="12" y="10" width="12" height="16" fill="none" stroke="#222" stroke-width="1.8"/>
      <rect x="15" y="8.5" width="6" height="3" fill="#222"/>
      <path d="M14.5 15h7M14.5 18h7M14.5 21h7" stroke="#222" stroke-width="1.4"/>
    </svg>
    <span class="feature-label">Rental<br>Forms</span>
  </div>

  <div class="feature feature--audio">
    <svg class="feature-icon" viewBox="0 0 36 36" aria-hidden="true">
      <circle cx="18" cy="18" r="16" fill="#fff" stroke="#d8262e" stroke-width="3"/>
      <rect x="15" y="9" width="6" height="11" rx="3" fill="#222"/>
      <path d="M12 17a6 6 0 0 0 12 0M18 23v4M15 27h6" fill="none" stroke="#222" stroke-width="1.6"/>
    </svg>
    <span class="feature-label">Audio<br>Podcasts</span>
  </div>
</section>

<section class="card-back" aria-label="Postcard back">
  <div class="brand">
    <span class="brand-mark" aria-hidden="true"></span>
    <span class="brand-name">Ted Harwick International</span>
  </div>

  <div class="message">
    <h2 class="message-headline">100’s of tips, tools and templates for you to use in your dealership.</h2>
    <p class="message-body">THI brings the daily tools you need to you in training videos, on-line resources and downloads. THI on-line webinars and support materials offer a library of learning right at your fingertips</p>
    <p class="contact">
      <span class="accent">For more information, please<br>contact us today</span><br>
      Phone: 1.800.555.0142<br>
      Email: info@tedharwick.net<br>
      <span class="accent">OR REGISTER ONLINE ON</span><br>
      tedharwick.net
    </p>
  </div>

  <div class="stamp-box" aria-hidden="true"></div>

  <ul class="address-lines" aria-hidden="true">
    <li></li><li></li><li></li><li></li><li></li>
  </ul>
</section>

</body>
</html>
```